Commercial Business Card - stand out, clean, simple, unique.

commercial real estate group located in Texas. Called 4 Ridges Real Estate. We want a unique yet clean and professional card. On one side I would like the 4R to be by itself or to look as unique or tasteful as possible. We have the logo in white, black, and color in case a black background or something similar looks best on one side. We need a space for our name, email, cell. website. And possibly room for a phrase or city.

Contact Information for Business Card

Name, Title, Email, Phone Number, website

```html
<!DOCTYPE html>
<html lang="en">
<head>
<meta charset="utf-8">
<title>4 Ridges Real Estate – Business Card</title>
<link href="https://fonts.googleapis.com/css2?family=Cinzel:wght@600&family=Lato:wght@400;700&display=swap" rel="stylesheet">
<style>
  :root {
    --canvas: #d9d9db;
    --paper: #ffffff;
    --ink-blue: #1f3c9a;
    --ink-text: #3a3a3a;
    --accent-orange: #e8832c;
    --card-black: #1a1a1c;
    --band-grey: #3a3a3d;
    --band-dark: #121214;
  }
  * { margin: 0; padding: 0; box-sizing: border-box; }
  html, body { width: 1200px; height: 900px; overflow: hidden; }
  body {
    background: var(--canvas);
    font-family: "Lato", Arial, sans-serif;
    position: relative;
  }
  .card {
    position: absolute;
    left: 250px;
    width: 700px;
    height: 400px;
  }
  /* Front */
  .card-front {
    top: 40px;
    background: var(--paper);
    border-bottom: 7px solid var(--accent-orange);
    border-left: 4px solid var(--accent-orange);
  }
  .front-brand {
    position: absolute;
    left: 60px;
    top: 176px;
    display: flex;
    align-items: center;
    gap: 12px;
  }
  .brand-square {
    width: 22px; height: 22px;
    background: var(--ink-blue);
  }
  .brand-name {
    font-family: "Cinzel", Georgia, serif;
    font-weight: 600;
    font-size: 24px;
    color: var(--ink-blue);
    letter-spacing: 0.5px;
  }
  .front-rule {
    position: absolute;
    left: 378px;
    top: 95px;
    width: 2px;
    height: 200px;
    background: var(--ink-blue);
  }
  .contact-block {
    position: absolute;
    left: 405px;
    top: 92px;
    color: var(--ink-text);
    font-size: 15px;
    line-height: 1.45;
  }
  .person-name {
    font-family: "Cinzel", Georgia, serif;
    font-weight: 600;
    font-size: 25px;
    color: var(--ink-blue);
    line-height: 1.1;
  }
  .person-title { font-size: 16px; margin-bottom: 14px; }
  .address { margin-bottom: 12px; }
  .contact-line { display: flex; align-items: center; gap: 8px; }
  .contact-line svg { width: 12px; height: 12px; flex: none; }
  .web-link { color: var(--ink-blue); }
  /* Back */
  .card-back {
    top: 470px;
    background: var(--card-black);
    overflow: hidden;
  }
  .back-texture {
    position: absolute; inset: 0;
    background: linear-gradient(160deg, #151517 0%, #2b2b2e 55%, #3b3b3e 100%);
  }
  .back-band {
    position: absolute;
    left: 0; right: 0;
    top: 150px; height: 110px;
    background: linear-gradient(90deg, var(--band-grey) 0%, #2a2a2d 50%, var(--band-dark) 100%);
    display: flex;
    align-items: center;
    justify-content: center;
    gap: 16px;
  }
  .back-band .brand-square { width: 28px; height: 28px; background: #2f4fb8; }
  .back-band .brand-name { font-size: 36px; color: #2f4fb8; }
</style>
</head>
<body>
  <section class="card card-front">
    <div class="front-brand">
      <span class="brand-square"></span>
      <span class="brand-name">4 Ridges Real Estate</span>
    </div>
    <div class="front-rule"></div>
    <div class="contact-block">
      <p class="person-name">DANIEL HARPER</p>
      <p class="person-title">Director</p>
      <p class="address">1450 Cedar Bend Lane<br>Austin, TX 78701</p>
      <p class="contact-line">
        <svg viewBox="0 0 12 12"><path d="M3 1 L5 3.5 L4 5 Q5.5 7.5 7 8 L8.5 7 L11 9 L9.5 11 Q4 10.5 1 2.5 Z" fill="#1f3c9a"/></svg>
        (512) 555-0148
      </p>
      <p class="contact-line">
        <svg viewBox="0 0 12 12"><rect x="1" y="2.5" width="10" height="7" fill="none" stroke="#1f3c9a" stroke-width="1.2"/><path d="M1 2.5 L6 6.5 L11 2.5" fill="none" stroke="#1f3c9a" stroke-width="1.2"/></svg>
        info@4ridgesrealestate.com
      </p>
      <p class="contact-line">
        <svg viewBox="0 0 12 12"><circle cx="6" cy="6" r="5" fill="none" stroke="#1f3c9a" stroke-width="1.2"/><path d="M1 6 H11 M6 1 Q3 6 6 11 Q9 6 6 1" fill="none" stroke="#1f3c9a" stroke-width="1"/></svg>
        <span class="web-link">www.4ridgesrealestate.com</span>
      </p>
    </div>
  </section>

  <section class="card card-back">
    <div class="back-texture" role="img" aria-label="Embossed repeating brand monogram pattern in dark grey"></div>
    <div class="back-band">
      <span class="brand-square"></span>
      <span class="brand-name">4 Ridges Real Estate</span>
    </div>
  </section>
</body>
</html>
```